依頼詳細
当サイトに店舗情報等を掲載してもらうための店舗への説明用チラシのデザイン制作をお願い致します。思わず掲載をしたくなるようなデザインをお願いします。シンプルでわかり易いものが希望です。
記載項目
サイト名はsemu(セム)・店舗情報掲載料1P21,000円/年額 複数P(写真・メニュー・クーポン等)42,000円/年額 求人情報掲載無料・採用時31,500円 当サイトの収益は児童養護施設等の子供達の学習支援に使われます。
サイズ
A4
ページ数
片面
希望イメージ
シンプル 複雑
単色 カラフル
暗い 明るい
日常 高級
遊び心 厳粛
未来的 伝統的
女性的 男性的
希望する色
オレンジ
納品ファイル
• 高解像度JPG (.jpg)
• イラストレーター形式 (.ai)
補足説明
《選ぶワクワクを全ての人に》をミッションにしたNPOです。この度開設するサイトを通じて、大人の生活の選択肢を増やし、学習支援によって子どもの将来の選択肢を増やすことを目的としています。サイト開設にあたっては、一定数の店舗登録が必須なため、店舗への説明がわかりやすい営業用チラシが必要です。イメージとしてはひらけ堂やぽみたすが近いかと思います。

```html
<!DOCTYPE html>
<html lang="ja">
<head>
<meta charset="utf-8">
<title>semu 加盟店募集チラシ</title>
<link rel="stylesheet" href="https://fonts.googleapis.com/css2?family=M+PLUS+Rounded+1c:wght@500;800&family=Noto+Sans+JP:wght@400;700;900&display=swap">
<style>
  :root{
    --orange:#f39a1e;
    --orange-deep:#e8810c;
    --green:#7cc243;
    --green-deep:#4f9a2a;
    --sky-top:#8fd0ef;
    --sky-bottom:#e9f6fb;
    --red:#e33a2c;
    --ink:#333;
    --white:#fff;
  }
  *{margin:0;padding:0;box-sizing:border-box}
  html,body{width:855px;height:1200px;overflow:hidden;background:#fff}
  body{font-family:"Noto Sans JP",sans-serif;color:var(--ink)}
  .flyer{position:relative;width:855px;height:1200px;overflow:hidden;background:#fff}

  .header{position:absolute;left:0;top:0;width:855px;height:222px;background:var(--orange)}
  .headline-top{position:absolute;left:40px;top:18px;font:900 54px/1 "Noto Sans JP",sans-serif;color:var(--white);letter-spacing:1px;white-space:nowrap}
  .headline-main{position:absolute;left:36px;top:92px;display:flex;align-items:baseline;white-space:nowrap;color:var(--white);font:900 50px/1 "Noto Sans JP",sans-serif}
  .site-name{position:relative;font:800 92px/1 "M PLUS Rounded 1c",sans-serif;color:var(--green);margin-right:8px}
  .site-name-ruby{position:absolute;right:-6px;top:2px;font:700 15px/1 "Noto Sans JP",sans-serif;color:var(--white)}
  .tagline{position:absolute;left:40px;top:194px;font:700 16px/1 "Noto Sans JP",sans-serif;color:var(--white);white-space:nowrap}
  .recruit-badge{position:absolute;right:20px;top:18px;background:var(--orange-deep);border:3px solid var(--white);color:var(--white);font:900 24px/1 "Noto Sans JP",sans-serif;padding:10px 16px;border-radius:8px}

  .sky{position:absolute;left:0;top:222px;width:855px;height:663px;background:linear-gradient(var(--sky-top),var(--sky-bottom))}
  .new-open{position:absolute;left:52px;top:268px;width:130px;height:130px}
  .tablet{position:absolute;left:290px;top:245px;width:480px;height:480px;border-radius:24px;background:linear-gradient(135deg,#3a3a3a,#151515);padding:24px}
  .tablet-screen{width:100%;height:100%;border-radius:6px;background:linear-gradient(160deg,#f4eadc,#e0c7a2 55%,#c98952)}
  .mission{position:absolute;left:40px;top:492px;width:240px;height:40px}
  .url{position:absolute;left:50px;top:608px;font:700 22px/1 "Noto Sans JP",sans-serif;color:var(--red);white-space:nowrap}
  .intro{position:absolute;left:50px;top:658px;font:400 15px/1.75 "Noto Sans JP",sans-serif;color:var(--ink);white-space:nowrap}
  .town{position:absolute;left:0;top:810px;width:855px;height:75px;background:linear-gradient(#a8d86b,var(--green))}

  .fees{position:absolute;left:0;top:885px;width:855px;height:190px;background:var(--green-deep)}
  .fees-lead{position:absolute;left:38px;top:14px;font:700 16px/1 "Noto Sans JP",sans-serif;color:var(--white);white-space:nowrap}
  .fee-table{position:absolute;left:38px;top:42px;width:600px;border-collapse:collapse;background:var(--white)}
  .fee-table td{border:1px solid var(--green-deep);padding:8px 10px;font:700 16px/1.2 "Noto Sans JP",sans-serif;white-space:nowrap}
  .fee-table .price{text-align:right;color:var(--red);font-size:20px;width:200px}
  .fee-table .price small{color:var(--ink);font-size:14px;font-weight:400}
  .charity-note{position:absolute;left:668px;top:42px;width:167px;height:118px;background:var(--white);border-radius:10px;padding:12px;font:400 13px/1.6 "Noto Sans JP",sans-serif;color:var(--ink)}
  .flowers{position:absolute;left:720px;top:1040px;width:110px;height:42px;border-radius:21px 21px 0 0;background:linear-gradient(90deg,#f7a8c4,#fbe27a,#f48a8a)}

  .contact{position:absolute;left:0;top:1075px;width:855px;height:125px}
  .contact-label{position:absolute;left:30px;top:16px;background:var(--orange);color:var(--white);font:700 15px/1 "Noto Sans JP",sans-serif;padding:7px 14px;border-radius:4px}
  .org-name{position:absolute;left:40px;top:62px;font:900 36px/1 "Noto Sans JP",sans-serif;color:var(--ink);white-space:nowrap}
  .org-info{position:absolute;left:420px;top:48px;font:700 16px/1.8 "Noto Sans JP",sans-serif;color:var(--ink);white-space:nowrap}
</style>
</head>
<body>
<main class="flyer">
  <header class="header">
    <p class="headline-top">あなたのお店を</p>
    <h1 class="headline-main"><span class="site-name">semu<span class="site-name-ruby">セム</span></span>に掲載にしませんか？</h1>
    <p class="tagline">セムは緑ヶ丘県みなと市の地域情報ポータルサイトです</p>
    <p class="recruit-badge">加盟店募集</p>
  </header>

  <section class="sky"></section>

  <svg class="new-open" viewBox="0 0 120 120" aria-label="NEW OPEN">
    <circle cx="60" cy="60" r="56" fill="var(--red)"/>
    <circle cx="60" cy="60" r="48" fill="none" stroke="#fff" stroke-width="2" stroke-dasharray="4 4"/>
    <text x="60" y="56" text-anchor="middle" fill="#fff" font-family="Noto Sans JP, sans-serif" font-weight="900" font-size="22">NEW</text>
    <text x="60" y="80" text-anchor="middle" fill="#fff" font-family="Noto Sans JP, sans-serif" font-weight="900" font-size="22">OPEN</text>
  </svg>

  <div class="tablet"><div class="tablet-screen" role="img" aria-label="タブレットに表示されたsemuサイトの画面写真"></div></div>

  <svg class="mission" viewBox="0 0 240 40" aria-label="選ぶワクワクを全ての人に">
    <polygon points="0,0 240,0 228,20 240,40 0,40 12,20" fill="var(--green-deep)"/>
    <text x="120" y="27" text-anchor="middle" fill="#fff" font-family="Noto Sans JP, sans-serif" font-weight="700" font-size="17">選ぶワクワクを全ての人に</text>
  </svg>

  <p class="url">http://www.semu.zzzzz</p>
  <p class="intro">この度開設するサイトを通じて<br>大人の生活の選択肢を増やし<br>学習支援によって<br>子どもの将来の選択肢を増やすことを<br>目的としています</p>

  <div class="town" role="img" aria-label="緑色の街並みのシルエットイラスト"></div>

  <section class="fees">
    <p class="fees-lead">地域のイベント情報や店舗情報等様々なコンテンツを掲載します</p>
    <table class="fee-table">
      <tr><td>店舗情報掲載料1P</td><td class="price">21,000円<small> / 年額</small></td></tr>
      <tr><td>複数P（写真・メニュー・クーポン等）</td><td class="price">42,000円<small> / 年額</small></td></tr>
      <tr><td>求人情報掲載無料</td><td class="price">31,500円<small> / 採用時</small></td></tr>
    </table>
    <p class="charity-note">当サイトの収益は児童養護施設等の子供達の学習支援に使われます。</p>
  </section>

  <div class="flowers" role="img" aria-label="花のイラスト"></div>

  <section class="contact">
    <p class="contact-label">お問い合わせ</p>
    <p class="org-name">○○○NPO 法人</p>
    <p class="org-info">住所：〒123-4567 緑ヶ丘県みなと市□□□<br>TEL：000-000-0000</p>
  </section>
</main>
</body>
</html>
```